Brochure and Business Card design

I am looking for a high end, elegant A4, 4 page brochure booklet to convey our products to clientele that will be visiting a luxury display showroom.

Harbourline Guard and Grilles is a Australian security provider, and we supply high end products from reputable brands.
The brochure will be directed to clients building a new home with a partnered building company and will be accompanied with display boards of our products.

I am providing files of a document we have put together with the relevant information and some images to help along the way, we are not bound by the layout or style it has been drawn up and we wish to give you complete creative freedom putting the peaces together. I have also provided the files for our logo in two different colours, and a picture of a brochure we love the look of.

If you have any suggestions, we can likely come up with further images etc if it will help or even if you feel some should be removed, we are open to that also

Target Market(s)

Young familys, people building new luxury homes, proffesionals, home owners

Industry/Entity Type

Business

Font styles to use
Serif
Sans Serif

Requirements
Must have
• All 8 pages
Should not have
• Not really a fan of reds and similar.

```html
<!DOCTYPE html>
<html lang="en">
<head>
<meta charset="utf-8">
<title>Harbourline Guard and Grilles – Product Brochure</title>
<link rel="stylesheet" href="https://fonts.googleapis.com/css2?family=Raleway:wght@300;400;600&family=Open+Sans:wght@400;600;700&display=swap">
<style>
:root{
  --bg:#b7b7b7;
  --paper:#ffffff;
  --paper-shade:#f1f1f1;
  --blue:#2a86c6;
  --blue-deep:#1f6fab;
  --green:#7fbf3f;
  --ink:#4a4a4a;
  --muted:#9a9a9a;
  --photo-grey:#8d9196;
  --photo-light:#d9dcdf;
}
*{margin:0;padding:0;box-sizing:border-box}
html,body{width:1200px;height:754px;overflow:hidden;background:var(--bg)}
body{position:relative;font-family:"Open Sans",sans-serif;color:var(--ink)}
.spread{position:absolute;width:540px;height:192px;display:flex;box-shadow:0 6px 14px rgba(0,0,0,.22)}
.spread-covers{left:30px;top:92px}
.spread-alarm{left:630px;top:92px}
.spread-screens{left:30px;top:469px}
.spread-vacuum{left:630px;top:469px}
.page{position:relative;width:270px;height:192px;background:var(--paper);overflow:hidden}
.page-left{background:linear-gradient(90deg,var(--paper) 85%,var(--paper-shade))}
.page-right{background:linear-gradient(90deg,var(--paper-shade),var(--paper) 15%)}
.abs{position:absolute}
.photo{position:absolute;background:linear-gradient(135deg,var(--photo-light),var(--photo-grey))}
.fill{position:absolute;inset:0;width:100%;height:100%}
.wordmark{font-family:"Raleway",sans-serif;font-weight:600;color:var(--ink);display:flex;align-items:center;gap:4px;letter-spacing:.5px}
.wordmark .dot{width:7px;height:7px;border-radius:50%;background:var(--blue)}
.small{font-size:4.2px;line-height:1.5;color:var(--muted)}
.heading{font-family:"Raleway",sans-serif;font-weight:300;color:var(--blue)}
.label{font-family:"Open Sans",sans-serif;font-weight:700;font-size:4.6px;color:var(--green);text-transform:uppercase}
.sub{font-family:"Open Sans",sans-serif;font-weight:600;font-size:4.8px;color:var(--blue)}
.sub-green{color:var(--green)}
.on-colour{color:#fff}
.thumb{position:absolute;background:linear-gradient(135deg,#e6e6e6,#b9bcbf);border-radius:1px}
.item-row{position:absolute;display:flex;gap:6px;align-items:flex-start}
.item-row .thumb{position:relative;flex:none}
</style>
</head>
<body>

<!-- Covers spread -->
<section class="spread spread-covers">
  <article class="page page-left back-cover">
    <div class="wordmark abs" style="left:88px;top:32px;font-size:8px"><span class="dot"></span>HARBOURLINE</div>
    <svg class="abs" style="left:0;top:54px" width="270" height="42" viewBox="0 0 270 42"><polygon points="0,0 270,0 252,42 0,42" fill="var(--blue)"/></svg>
    <p class="small on-colour abs" style="left:18px;top:60px;width:220px;text-align:center;color:#fff">We design, supply and install quality security products for new homes across every stage of the build.</p>
    <p class="small on-colour abs" style="left:18px;top:78px;width:220px;text-align:center;color:#fff">Our showroom team will help you choose the right finish for your lifestyle.</p>
    <p class="label abs" style="left:100px;top:118px;text-transform:none">For all inquiries</p>
    <p class="small abs" style="left:60px;top:127px;width:150px;text-align:center;color:var(--ink)">E: info@harbourlineguard.com.au &nbsp;|&nbsp; P: 1300 000 000</p>
    <p class="sub abs" style="left:70px;top:136px;width:130px;text-align:center">www.harbourlineguard.com.au</p>
    <p class="small abs" style="left:60px;top:172px;width:150px;text-align:center">All product images are for display purposes only.</p>
  </article>
  <article class="page page-right front-cover">
    <svg class="abs" style="left:0;top:40px" width="270" height="44" viewBox="0 0 270 44" role="img" aria-label="Row of home security product and house exterior photographs">
      <defs><linearGradient id="ph" x1="0" y1="0" x2="1" y2="1"><stop offset="0" stop-color="#cfd3d6"/><stop offset="1" stop-color="#6f757b"/></linearGradient></defs>
      <polygon points="30,0 82,0 58,44 6,44" fill="url(#ph)"/>
      <polygon points="92,0 144,0 120,44 68,44" fill="url(#ph)"/>
      <polygon points="154,0 206,0 182,44 130,44" fill="url(#ph)"/>
      <polygon points="216,0 250,0 226,44 192,44" fill="url(#ph)"/>
      <polygon points="260,0 270,0 270,44 236,44" fill="var(--green)"/>
    </svg>
    <div class="wordmark abs" style="left:88px;top:138px;font-size:10px"><span class="dot"></span>HARBOURLINE</div>
    <p class="small abs" style="left:92px;top:156px">www.harbourlineguard.com.au</p>
  </article>
</section>

<!-- Alarm and intercom spread -->
<section class="spread spread-alarm">
  <article class="page page-left alarm-page">
    <h2 class="heading abs" style="left:16px;top:12px;font-size:11px">Alarm Systems</h2>
    <p class="small abs" style="left:16px;top:30px;width:100px">Protect your family with a monitored alarm system built around your new home plan and daily routine.</p>
    <div class="photo" style="left:130px;top:12px;width:140px;height:46px" role="img" aria-label="Alarm keypad mounted on an interior wall"></div>
    <p class="label abs" style="left:130px;top:62px;text-transform:none">Home kit</p>
    <div class="abs" style="left:120px;top:70px;width:150px;height:14px;background:var(--blue)"></div>
    <p class="small abs" style="left:126px;top:73px;color:#fff">Arm and disarm your system from anywhere with the app.</p>
    <p class="label abs" style="left:16px;top:96px">Popular upgrades</p>
    <div class="thumb" style="left:16px;top:108px;width:16px;height:16px" role="img" aria-label="Motion sensor"></div>
    <p class="small abs" style="left:36px;top:112px">Motion sensor</p>
    <div class="thumb" style="left:72px;top:108px;width:16px;height:16px" role="img" aria-label="Smoke detector"></div>
    <p class="small abs" style="left:92px;top:112px">Smoke detector</p>
    <div class="thumb" style="left:130px;top:108px;width:16px;height:16px" role="img" aria-label="Remote keyfob"></div>
    <p class="small abs" style="left:150px;top:112px">Remote keyfob</p>
    <div class="thumb" style="left:16px;top:134px;width:16px;height:16px" role="img" aria-label="Door reed switch"></div>
    <p class="small abs" style="left:36px;top:138px">Door reed</p>
    <div class="thumb" style="left:72px;top:134px;width:16px;height:16px" role="img" aria-label="Outdoor siren"></div>
    <p class="small abs" style="left:92px;top:138px">Siren</p>
    <div class="thumb" style="left:130px;top:134px;width:16px;height:16px" role="img" aria-label="Panic button"></div>
    <p class="small abs" style="left:150px;top:138px">Panic button</p>
  </article>
  <article class="page page-right intercom-page">
    <div class="photo" style="left:0;top:0;width:270px;height:42px;background:linear-gradient(90deg,#ffffff,#e9eef2 50%,#c9b8a6)" role="img" aria-label="Bright modern hallway with intercom screen"></div>
    <h2 class="heading abs" style="left:20px;top:14px;font-size:11px">Intercom</h2>
    <p class="small abs" style="left:20px;top:46px;width:150px">Answer the door from any room and see who is calling before you open.</p>
    <div class="item-row" style="left:20px;top:66px">
      <div class="thumb" style="width:18px;height:14px" role="img" aria-label="Seven inch video intercom"></div>
      <div><p class="sub">7 inch video intercom</p><p class="small">Hands free colour screen with night vision.</p></div>
    </div>
    <div class="item-row" style="left:20px;top:96px">
      <div class="thumb" style="width:18px;height:14px" role="img" aria-label="Compact video intercom"></div>
      <div><p class="sub">4.3 inch video intercom</p><p class="small">Hands free colour screen with night vision.</p></div>
    </div>
    <div class="item-row" style="left:20px;top:126px">
      <div class="thumb" style="width:18px;height:14px" role="img" aria-label="Audio intercom handset"></div>
      <div><p class="sub">Audio only intercom</p><p class="small">Hands free colour screen with night vision.</p></div>
    </div>
    <p class="label abs" style="left:188px;top:50px">Popular upgrades</p>
    <div class="thumb" style="left:188px;top:62px;width:14px;height:16px" role="img" aria-label="Indoor monitor"></div>
    <p class="small abs" style="left:206px;top:66px;width:58px">Extra indoor monitor</p>
    <div class="thumb" style="left:188px;top:90px;width:14px;height:16px" role="img" aria-label="Electric strike lock"></div>
    <p class="small abs" style="left:206px;top:94px;width:58px">Electric strike lock</p>
    <div class="thumb" style="left:188px;top:118px;width:14px;height:16px" role="img" aria-label="Handset"></div>
    <p class="small abs" style="left:206px;top:122px;width:58px">Handset with memory</p>
  </article>
</section>

<!-- Security screens spread -->
<section class="spread spread-screens">
  <article class="page page-left screens-intro">
    <svg class="fill" viewBox="0 0 270 192" role="img" aria-label="Close-up of a security screen door with stainless mesh and handle">
      <defs>
        <linearGradient id="mesh" x1="0" y1="0" x2="1" y2="1"><stop offset="0" stop-color="#e4e6e8"/><stop offset=".6" stop-color="#5e6367"/><stop offset="1" stop-color="#2e3134"/></linearGradient>
        <radialGradient id="glow" cx=".55" cy=".55" r=".5"><stop offset="0" stop-color="#6fb3e3"/><stop offset="1" stop-color="var(--blue-deep)"/></radialGradient>
      </defs>
      <rect width="270" height="120" fill="url(#mesh)"/>
      <path d="M0,112 Q140,48 270,62 L270,192 L0,192 Z" fill="url(#glow)"/>
    </svg>
    <h2 class="heading abs on-colour" style="left:96px;top:90px;font-size:11px;color:#fff">Why Nightbar Shield?</h2>
    <p class="small abs" style="left:96px;top:108px;width:150px;color:#e6f1fa">Our stainless steel mesh screens stop intruders while keeping airflow and views open.</p>
  </article>
  <article class="page page-right screens-features">
    <div class="item-row" style="left:22px;top:18px">
      <svg width="22" height="14" viewBox="0 0 22 14" role="img" aria-label="Mesh sample"><polygon points="0,14 11,0 22,14" fill="#c5c8cb"/></svg>
      <div><p class="sub sub-green">Strength</p><p class="small" style="width:190px">Tested to Australian standards for impact, knife and jemmy resistance.</p></div>
    </div>
    <div class="item-row" style="left:22px;top:58px">
      <svg width="22" height="14" viewBox="0 0 22 14" role="img" aria-label="Mesh sample"><polygon points="0,14 11,0 22,14" fill="#c5c8cb"/></svg>
      <div><p class="sub sub-green">Visibility</p><p class="small" style="width:190px">Tested to Australian standards for impact, knife and jemmy resistance.</p></div>
    </div>
    <div class="item-row" style="left:22px;top:98px">
      <svg width="22" height="14" viewBox="0 0 22 14" role="img" aria-label="Mesh sample"><polygon points="0,14 11,0 22,14" fill="#c5c8cb"/></svg>
      <div><p class="sub sub-green">Insect control</p><p class="small" style="width:190px">Tested to Australian standards for impact, knife and jemmy resistance.</p></div>
    </div>
    <div class="item-row" style="left:22px;top:138px">
      <svg width="22" height="14" viewBox="0 0 22 14" role="img" aria-label="Mesh sample"><polygon points="0,14 7,4 12,10 16,2 22,14" fill="#c5c8cb"/></svg>
      <div><p class="sub sub-green">Custom design</p><p class="small" style="width:190px">Tested to Australian standards for impact, knife and jemmy resistance.</p></div>
    </div>
  </article>
</section>

<!-- Ducted vacuum spread -->
<section class="spread spread-vacuum">
  <article class="page page-left vacuum-intro">
    <svg class="fill" viewBox="0 0 270 192">
      <defs>
        <linearGradient id="family" x1="0" y1="0" x2="1" y2="0"><stop offset="0" stop-color="#eef1f4"/><stop offset="1" stop-color="#d8c4b4"/></linearGradient>
        <radialGradient id="greenglow" cx=".5" cy=".5" r=".6"><stop offset="0" stop-color="#a8d57a"/><stop offset="1" stop-color="#6fb032"/></radialGradient>
      </defs>
      <rect width="270" height="120" fill="url(#family)" role="img" aria-label="Smiling family relaxing together at home"/>
      <path d="M0,110 Q150,50 270,68 L270,192 L0,192 Z" fill="url(#greenglow)"/>
    </svg>
    <div class="photo" style="left:16px;top:70px;width:70px;height:30px;background:linear-gradient(135deg,#6a6f73,#2c2f31);border-radius:2px" role="img" aria-label="Vacuum hose and cleaning tool kit"></div>
    <h2 class="heading abs" style="left:120px;top:88px;font-size:11px;color:#fff">Ducted Vacuum</h2>
    <p class="small abs" style="left:120px;top:106px;width:130px;color:#f0f8e6">Cleaner air for the whole family with powerful suction ducted to every room.</p>
  </article>
  <article class="page page-right vacuum-features">
    <div class="photo" style="left:20px;top:30px;width:56px;height:80px;border-radius:8px;background:linear-gradient(90deg,#5c6268,#9aa0a5 45%,#4d5257)" role="img" aria-label="Ducted vacuum power unit"></div>
    <p class="sub sub-green abs" style="left:96px;top:24px">No dust left behind</p>
    <p class="small abs" style="left:96px;top:31px;width:76px">Dust and allergens are carried out of living areas to the garage unit.</p>
    <p class="sub sub-green abs" style="left:96px;top:76px">Quiet in every room</p>
    <p class="small abs" style="left:96px;top:83px;width:76px">Dust and allergens are carried out of living areas to the garage unit.</p>
    <p class="sub sub-green abs" style="left:184px;top:24px">Easy hose storage</p>
    <p class="small abs" style="left:184px;top:31px;width:76px">Dust and allergens are carried out of living areas to the garage unit.</p>
    <p class="sub sub-green abs" style="left:184px;top:76px">Five year warranty</p>
    <p class="small abs" style="left:184px;top:83px;width:76px">Dust and allergens are carried out of living areas to the garage unit.</p>
  </article>
</section>

</body>
</html>
```